Wireless Captive Portal Provider needs a logo and business card design

We need a logo and business card for a new company called Pebblecrest WiFi LLC. The company offers a cloud base service for businesses to provide wireless access to their customers, this is called a captive portal. The captive portal also has the ability to encourage users to check in or tweet at the company which is a major draw so there is a large social media component to the company. We would like to see designs that incorporate the name of the company. We are envisioning a minimalist design, but will entertain any original ideas, especially those that incorporate the social media component.

The company name is Pebblecrest WiFi, so a light a fresh look is desired in the blue and yellow color scheme.

We own www.pebblecrestwifi.example domain name for our site and email as well as @PebblecrestWiFi on twitter. I mention this as this allows us to do the clever business card design that can capture email, twitter, and homepage on a business card. Search google images for "business card twitter email website" for examples.

I would be interested in business card designs that allow for an image of the employee to be added.

Target Market(s)

Our target market are store fronts with customer seating that provide wireless access. Or anywhere we wireless access is provided.

Industry/Entity Type

Business

Contact Information for Business Card

Logo Text

Pebblecrest WiFi, Ltd. Liability Co.

Logo styles of interest
Pictorial/Combination Logo
Abstract Logo
Font styles to use
Sans Serif

Colors
85cae6
fbf289
cadf82
33a6d7
fbee3e
add136
0891cc
fbed22
9bcb3b

Requirements
Nice to have
• We own www.pebblecrestwifi.example domain name for our site and email as well as @PebblecrestWiFi on twitter. I mention this as this allows us to do the clever business card design that can capture email, twitter, and homepage on a business card. Search google images for "business card twitter email website" for examples.

```html
<!DOCTYPE html>
<html lang="en">
<head>
<meta charset="utf-8">
<title>Pebblecrest WiFi — Business Card</title>
<link rel="stylesheet" href="https://fonts.googleapis.com/css2?family=Josefin+Sans:wght@600;700&display=swap">
<style>
  :root {
    --page: #ffffff;
    --card: #e9d9a9;
    --card-deep: #e2cf9a;
    --teal: #17798a;
    --orange: #e8901f;
    --orange-soft: rgba(240, 170, 70, 0.45);
    --teal-soft: rgba(120, 170, 160, 0.5);
  }
  * { box-sizing: border-box; margin: 0; padding: 0; }
  html, body {
    width: 1200px; height: 1000px; overflow: hidden;
    background: var(--page);
    font-family: "Josefin Sans", sans-serif;
  }
  .card {
    position: absolute; left: 75px; top: 200px;
    width: 1050px; height: 600px; overflow: hidden;
    background: radial-gradient(ellipse at 70% 40%, var(--card) 0%, var(--card-deep) 100%);
  }
  .brand-backdrop {
    position: absolute; left: 0; top: 0; width: 680px; height: 600px;
    background:
      radial-gradient(circle at 330px 360px, var(--teal-soft) 0 140px, transparent 142px),
      radial-gradient(ellipse at 200px 420px, var(--orange-soft) 0 300px, transparent 420px);
    opacity: 0.55;
  }
  .brand {
    position: absolute; left: 83px; top: 40px;
    display: flex; flex-direction: column; align-items: center; gap: 48px;
  }
  .brand-dot {
    width: 110px; height: 110px; border-radius: 50%;
    background: var(--teal);
  }
  .brand-name {
    font-weight: 600; font-size: 38px; letter-spacing: 4px;
    color: var(--orange); white-space: nowrap;
  }
  .contact {
    position: absolute; left: 295px; top: 440px;
    font-weight: 700; text-transform: uppercase;
  }
  .email-wrap { position: relative; height: 36px; }
  .email, .ghost {
    position: absolute; left: 0; top: 0;
    font-size: 30px; letter-spacing: 2px; white-space: nowrap; line-height: 36px;
  }
  .email { color: var(--teal); }
  .email .accent { color: var(--orange); }
  .ghost { color: transparent; }
  .mark { position: relative; }
  .mark::before {
    content: ""; position: absolute; left: 2px; right: 4px;
    bottom: 100%; border: 3px solid var(--orange); border-bottom: none;
  }
  .mark::after {
    content: attr(data-label); position: absolute;
    font-size: 21px; letter-spacing: 2px; color: var(--orange);
    background: var(--card); padding: 0 4px; line-height: 20px;
  }
  .mark.name::before { height: 12px; }
  .mark.name::after { right: 100%; bottom: calc(100% + 2px); margin-right: -8px; background: transparent; }
  .mark.twitter::before { height: 16px; }
  .mark.twitter::after { left: 50%; bottom: calc(100% + 6px); transform: translateX(-30%); }
  .mark.site::before { height: 46px; }
  .mark.site::after { left: 50%; bottom: calc(100% + 36px); transform: translateX(-80%); }
  .person {
    font-size: 30px; letter-spacing: 2px; color: var(--teal); line-height: 40px;
  }
  .role {
    margin-top: 4px; font-size: 24px; letter-spacing: 2px; color: var(--orange);
  }
  .phone {
    margin-top: 6px; font-size: 21px; letter-spacing: 1.5px; color: var(--teal);
  }
  .phone .label { color: var(--orange); margin-right: 6px; }
</style>
</head>
<body>
  <section class="card">
    <div class="brand-backdrop" role="img" aria-label="Faint enlarged brand mark decoration in soft orange and sage tones"></div>

    <div class="brand">
      <div class="brand-dot"></div>
      <div class="brand-name">PEBBLECREST WIFI</div>
    </div>

    <div class="contact">
      <div class="email-wrap">
        <div class="ghost" aria-hidden="true">DEREK@<span class="mark site" data-label="SITE">PEBBLECRESTWIFI.EXAMPLE</span></div>
        <div class="ghost" aria-hidden="true">DEREK<span class="mark twitter" data-label="TWITTER">@PEBBLECRESTWIFI</span></div>
        <div class="ghost" aria-hidden="true"><span class="mark name" data-label="NAME">DEREK</span></div>
        <div class="email">DEREK@<span class="accent">PEBBLECREST</span>WIFI.EXAMPLE</div>
      </div>
      <div class="person">MARLOWE</div>
      <div class="role">FOUNDER</div>
      <div class="phone"><span class="label">PHONE</span>1-555-014-2290</div>
    </div>
  </section>
</body>
</html>
```